Professional banners for an eyewear company

I have 3 images which need to be made into banners. Size 990 x 370, with a 10 pixel white border at top and bottom of banner.

They all need to be adjusted to make the colours better and less bright.
All will need some writing written on them with a nice serif font.

Banner 1 text: Handcrafted luxury eyewear, with a purpose...
Banner 2 text: Half of our profits go to help malnourished children in India
Banner 3 text: 10% of your first order, use code: First Order

On our homepage these 3 banners will alternate, so they need to look good together.

Tips
Please take a look at the banners on the lunvoreck.com homepage, this is kind of how I want the text to be displayed, and they use good colours.

The backgrounds on Banners 2 & 3 can be changed.
Banner 3 background if you can change to a nice colour, as per lunvoreck.com homepage.
Updates

Hi, just a quick update, thank you for all the designs submitted so far, please keep in mind that the brand is a luxury high-end brand so designs will need to reflect this.

Industry/Entity Type

Eyewear

```html
<!DOCTYPE html>
<html lang="en">
<head>
<meta charset="UTF-8">
<title>First Order Offer Banner</title>
<link href="https://fonts.googleapis.com/css2?family=Roboto+Slab:wght@400;500&display=swap" rel="stylesheet">
<style>
  :root {
    --canvas: #f7f4f0;
    --canvas-light: #fbfaf8;
    --stripe: rgba(225, 218, 210, 0.35);
    --accent: #e03a55;
    --gold: #b98a5c;
    --rule: #d9c3ab;
    --photo-light: #f1ece6;
    --photo-mid: #d8b49a;
    --photo-dark: #b46a43;
  }
  * { margin: 0; padding: 0; box-sizing: border-box; }
  html, body { width: 1200px; height: 448px; overflow: hidden; background: var(--canvas); }
  .banner {
    position: relative;
    width: 1200px;
    height: 448px;
    overflow: hidden;
    font-family: "Roboto Slab", Georgia, serif;
    background:
      linear-gradient(90deg, transparent 0%, transparent 45%, var(--canvas) 75%),
      repeating-linear-gradient(180deg, var(--canvas-light) 0 9px, var(--stripe) 9px 12px),
      var(--canvas);
  }
  .banner__photo {
    position: absolute;
    left: 188px;
    top: 0;
    width: 300px;
    height: 448px;
    background: linear-gradient(180deg, var(--photo-dark) 0%, var(--photo-mid) 35%, var(--photo-light) 55%, var(--photo-light) 100%);
    border-radius: 120px 120px 0 0;
    opacity: 0.85;
  }
  .offer {
    position: absolute;
    left: 560px;
    width: 486px;
    top: 148px;
    text-align: center;
  }
  .offer__headline {
    color: var(--accent);
    font-weight: 500;
    line-height: 1;
    letter-spacing: 0.5px;
  }
  .offer__percent { font-size: 56px; }
  .offer__off { font-size: 42px; margin-left: 4px; }
  .offer__code {
    margin-top: 8px;
    color: var(--gold);
    font-size: 26px;
    font-weight: 400;
    line-height: 1.2;
  }
  .offer__cta {
    margin-top: 16px;
    display: flex;
    align-items: center;
    justify-content: center;
    gap: 14px;
    color: var(--accent);
    font-size: 14.5px;
    font-weight: 500;
    letter-spacing: 0.6px;
    text-transform: uppercase;
  }
  .offer__rule { width: 56px; height: 1px; background: var(--rule); }
</style>
</head>
<body>
  <div class="banner">
    <div class="banner__photo" role="img" aria-label="Red-haired model in sunglasses and a polka-dot blouse"></div>
    <div class="offer">
      <h1 class="offer__headline"><span class="offer__percent">10%</span><span class="offer__off">OFF</span></h1>
      <p class="offer__code">Your First Order, Use Code: First Order</p>
      <p class="offer__cta"><span class="offer__rule"></span>Shop the Collection<span class="offer__rule"></span></p>
    </div>
  </div>
</body>
</html>
```